ashby paving works

Needs to have phone number 0412885107 and email marklowry@pavemail.com.au.
ABN 27613048852
name mark lowry

For all your concreting solutions
Excavation
Exposed & colour concrete
House & shed slabs
Driveways
Landing & steps

Contact Information for Business Card

ph 0412885107
email marklowry@pavemail.com.au.
ABN 27613048852
name mark lowry

```html
<!DOCTYPE html>
<html lang="en">
<head>
<meta charset="utf-8">
<title>Ashby Paving Works – Business Card</title>
<link href="https://fonts.googleapis.com/css2?family=Oswald:wght@300;400;600;700&family=Montserrat:wght@600&display=swap" rel="stylesheet">
<style>
  :root {
    --page: #ffffff;
    --card: #282828;
    --orange: #f26a24;
    --grey: #6e6e6e;
    --text: #ffffff;
    --faint: #48342e;
  }
  html, body { margin: 0; padding: 0; overflow: hidden; }
  body { width: 1200px; height: 1200px; background: var(--page); position: relative; font-family: "Oswald", sans-serif; }
  .card { position: absolute; background: var(--card); overflow: hidden; }
  .card--front { left: 260px; top: 148px; width: 680px; height: 398px; }
  .card--back { left: 262px; top: 653px; width: 677px; height: 398px; }

  .brand-mark { position: absolute; left: 20px; top: 70px; width: 54px; height: 54px; background: var(--orange); }
  .brand-divider { position: absolute; left: 118px; top: 62px; width: 2px; height: 88px; background: var(--orange); }
  .brand-name { position: absolute; left: 126px; top: 84px; width: 240px; margin: 0; white-space: nowrap;
    font-family: "Montserrat", sans-serif; font-weight: 600; font-size: 17px; line-height: 1.2; letter-spacing: -0.3px; color: var(--orange); text-transform: uppercase; }
  .brand-phone { position: absolute; left: 126px; top: 112px; width: 184px; text-align: center; margin: 0; white-space: nowrap;
    font-family: "Montserrat", sans-serif; font-weight: 600; font-size: 12px; line-height: 1.2; letter-spacing: 2px; color: var(--orange); }

  .name-divider { position: absolute; left: 369px; top: 82px; width: 3px; height: 245px; background: var(--orange); }
  .person-name { position: absolute; left: 393px; top: 192px; margin: 0; font-weight: 700; font-size: 50px; line-height: 1; color: var(--orange); white-space: nowrap; }

  .contact { position: absolute; left: 32px; top: 244px; margin: 0; }
  .contact-divider { position: absolute; left: 83px; top: 246px; width: 2px; height: 86px; background: var(--orange); }
  .contact-row { display: flex; height: 31px; align-items: center; font-size: 23px; font-weight: 300; white-space: nowrap; }
  .contact-label { width: 58px; color: var(--orange); }
  .contact-value { color: var(--text); letter-spacing: -0.2px; }

  .accent-band { position: absolute; left: 2px; right: 0; top: 372px; height: 14px; background: var(--orange); }

  .backdrop-mark { position: absolute; left: 470px; top: 150px; width: 300px; height: 300px; background: var(--faint); opacity: 0.8; }
  .tagline { position: absolute; left: 40px; top: 82px; margin: 0; font-weight: 700; font-size: 40px; line-height: 1.2; color: var(--orange); white-space: nowrap; }
  .services { position: absolute; left: 39px; top: 150px; margin: 0; padding: 0; list-style: none; }
  .service { display: flex; align-items: center; height: 39.5px; font-size: 29px; color: var(--text); white-space: nowrap; }
  .service-bullet { width: 27px; height: 20px; margin-right: 13px; flex: none; }
</style>
</head>
<body>
  <section class="card card--front">
    <div class="brand-mark"></div>
    <div class="brand-divider"></div>
    <p class="brand-name">Ashby Paving Works</p>
    <p class="brand-phone">0412885107</p>

    <div class="name-divider"></div>
    <h1 class="person-name">Mark Lowry</h1>

    <div class="contact-divider"></div>
    <div class="contact">
      <div class="contact-row"><span class="contact-label">Ph.</span><span class="contact-value">0412885107</span></div>
      <div class="contact-row"><span class="contact-label">Email</span><span class="contact-value">marklowry@pavemail.com.au.</span></div>
      <div class="contact-row"><span class="contact-label">ABN</span><span class="contact-value">27613048852</span></div>
    </div>

    <div class="accent-band"></div>
  </section>

  <section class="card card--back">
    <div class="backdrop-mark"></div>
    <h2 class="tagline">For all concreting solutions</h2>
    <ul class="services">
      <li class="service"><svg class="service-bullet" viewBox="0 0 27 20"><polygon points="13.5,0 27,10 0,10" fill="#f26a24"/><polygon points="0,11 27,11 13.5,20" fill="#6e6e6e"/></svg>Excavation</li>
      <li class="service"><svg class="service-bullet" viewBox="0 0 27 20"><polygon points="13.5,0 27,10 0,10" fill="#f26a24"/><polygon points="0,11 27,11 13.5,20" fill="#6e6e6e"/></svg>Exposed &amp; Colour Concrete</li>
      <li class="service"><svg class="service-bullet" viewBox="0 0 27 20"><polygon points="13.5,0 27,10 0,10" fill="#f26a24"/><polygon points="0,11 27,11 13.5,20" fill="#6e6e6e"/></svg>house &amp; Shed slabs</li>
      <li class="service"><svg class="service-bullet" viewBox="0 0 27 20"><polygon points="13.5,0 27,10 0,10" fill="#f26a24"/><polygon points="0,11 27,11 13.5,20" fill="#6e6e6e"/></svg>Driveways</li>
      <li class="service"><svg class="service-bullet" viewBox="0 0 27 20"><polygon points="13.5,0 27,10 0,10" fill="#f26a24"/><polygon points="0,11 27,11 13.5,20" fill="#6e6e6e"/></svg>Landing &amp; Steps</li>
    </ul>
  </section>
</body>
</html>
```